Website Redesign Project

Bright Harbor Planning provides project management and project controls consultancy services to companies in many industry sectors, within Australia and overseas. My company has been developing a business brand through forging strong business relationships within industry. We provide innovative tools, concepts and solutions to management teams to assist them in better plan and managing there project portfolios.
SECTORS OF INDUSTRY WE SERVICE
★Oil & Gas
★Minerals & Metals
★Petrochemical
★Manufacturing
★Building & Construction
★Telecommunications
★Rail
★Civil
OLD WEBSITE
My old website www.brightharborplanning.com.au needs a complete overhaul in terms of how the web pages look and feel. I am trying to get away from the grey, washed out look as it is uninviting and dull. My clients commented that my webpage does not reflect who I am as a company or my core values. Think total redesign
DESIGN
I would like a webpage design that is modern and has a corporate image. It must be elegant, classy, and have an overall glossy appearance. I want something exciting that creates some excellent feedback from clients. It needs to have a savvy appearance and an attitude of a market leader. A generic website template cannot be used as I provide a unique service to clients. I do not need a website design that looks like my compeditors, I want something that stands out in the crowd and effectivly markets my bussinesses brand. I want my website to represent quality, so only high resolution images that are clear, sharp and in focus can be used. With this design, throw your standard webpage design concepts out the window, as I want something fresh, innovative, exciting and inviting. The overall design should appear uncluttered as all content needs to be there for a reason, so think functional.
It must be professional and of the highest calibre as my clients expect nothing less. I provide clients with innovative tools, concepts and solutions, so the design needs to be edgy and creative to align with my company’s core business services. The new design must promote the company’s brand and us as a market leader. It must communicate that we service many industry sectors and reflect our company’s creativity, vision, energy and drive.
WEBPAGE WRITTEN CONTENT
I am happy with the written content on each page within my old website. You may arrange the text how you see fit within the new design. On the main page of my old website the text is under scored, I am not a big fan of this. I currently do not like the format the text is in, I am looking for a formatt that is easy to read, looks flattering and pleasing to the eye.
MAIN PAGE DESIGN
The main page design needs to focus on my company as a brand, it must promote that I service many industry sectors. My old webpage had me pigeon holed as only providing services to oil and gas. This is incorrect as I service oil & gas, metals and minerals, Petrochemical, Manufacturing, Building & Construction, Telecommunications, Rail and civil.
WEBPAGE COLUR PREFERENCE
Prefer a white background with plenty of colour
TESTIMONIAL TAB
The testimonial tab on the task bar can be removed as it is no longer required.
FINISHED PRODUCT
The finished product will be uploaded by you to a nominated web hosting account. I will need a copy of all files associated with the design. A copy of the finished product will also be provided in formats that can me imported to Xara Pro Designer as I will update my website in 6 months or so using this tool.
Updates
I have updated the design brief after recieving feedback from several designers
Thanks
Reason: Some designers have asked for more time
Hi All
I have just launched another project called "bright harbor planning business card redesign project", you are all welcome to join this project.
Thanks
Target Market(s)
★Oil and Gas
★Mining and Resources
★Building and infrastructure
★Petrochemical
★Civil and roads
★Rail
Industry/Entity Type
Industry
Requirements
Must have
- ★Draw you in
★Hold your attention
★Identify company brand
★Highlight skills experience and expertise
★Be a unique design not generic
Should not have
- ★The webpage design should not be old fashioned
★ The design should not be based off a generic design template
★The webpage should not be cluttered; everything needs to be there for a reason.

```html
<!DOCTYPE html>
<html lang="en">
<head>
<meta charset="utf-8">
<title>Bright Harbor Planning</title>
<link href="https://fonts.googleapis.com/css2?family=Ubuntu:wght@400;500;700&family=Open+Sans:wght@400&family=Arimo:wght@400&display=swap" rel="stylesheet">
<style>
  :root {
    --ink: #111111;
    --nav: #34506f;
    --text: #333333;
    --white: #ffffff;
    --brand-red: #c8161d;
    --brick: #9e2308;
    --orange: #e8890f;
    --footer-bg: #000000;
    --footer-text: #9a9a9a;
    --social-1: #3c5a99;
    --social-2: #f0a030;
    --social-3: #c4302b;
    --social-4: #4a8cc9;
  }
  * { box-sizing: border-box; margin: 0; padding: 0; }
  html, body { width: 1200px; height: 948px; overflow: hidden; background: var(--white); }
  body { position: relative; font-family: "Ubuntu", sans-serif; color: var(--text); }

  .brand { position: absolute; left: 146px; top: 44px; display: flex; align-items: center; gap: 10px; }
  .brand-dot { width: 30px; height: 30px; border-radius: 50%; background: var(--brand-red); }
  .brand-name { font-family: "Ubuntu", sans-serif; font-weight: 700; font-size: 24px; color: var(--ink); }

  .social { position: absolute; top: 55px; left: 877px; display: flex; gap: 16px; }
  .social span { width: 26px; height: 26px; border-radius: 50%; display: block; }
  .social .s1 { background: var(--social-1); }
  .social .s2 { background: var(--social-2); }
  .social .s3 { background: var(--social-3); }
  .social .s4 { background: var(--social-4); }

  .main-nav a { position: absolute; top: 105px; font-family: "Open Sans", sans-serif; font-size: 16px; color: var(--nav); text-decoration: none; }

  .hero { position: absolute; left: 108px; top: 133px; width: 966px; height: 373px;
    background: linear-gradient(100deg, #3b3836 0%, #5a5450 35%, #6b4a3a 60%, #a2492a 75%, #3a3533 100%); }
  .hero-caption { position: absolute; left: 44px; top: 163px; width: 487px; height: 136px; background: rgba(0,0,0,.62); padding: 10px 0 0 29px; }
  .hero-caption h1 { font-weight: 400; font-size: 37px; color: var(--white); line-height: 1.1; }
  .hero-caption p { margin-top: 8px; font-size: 15px; line-height: 17.5px; color: var(--white); width: 452px; }
  .btn { position: absolute; display: block; border-radius: 17px; font-family: "Arimo", sans-serif; color: var(--white); text-align: center; text-decoration: none; font-size: 16px; line-height: 33px; height: 33px; }
  .btn-vision { left: 364px; top: 282px; width: 142px; background: var(--brick); }
  .hero-arrows { position: absolute; left: 895px; top: 330px; }

  .section-title { position: absolute; font-weight: 400; font-size: 29px; color: var(--ink); }
  .news-title { left: 148px; top: 546px; }
  .news-thumb { position: absolute; left: 148px; top: 598px; width: 97px; height: 72px; background: linear-gradient(135deg, #c98a2a, #5c6c8a 60%, #d0b060); }
  .news-headline { position: absolute; left: 259px; top: 597px; width: 360px; font-weight: 500; font-size: 16px; line-height: 17px; color: var(--ink); }
  .news-body { position: absolute; left: 259px; top: 642px; width: 340px; font-size: 13px; line-height: 16.6px; color: var(--text); }
  .btn-more { left: 259px; top: 728px; width: 108px; background: var(--orange); }
  .btn-all { left: 375px; top: 728px; width: 95px; background: var(--brick); }

  .projects-title { left: 693px; top: 548px; }
  .sector-list { position: absolute; top: 597px; list-style: none; font-size: 12px; line-height: 16.6px; color: var(--text); }
  .sector-list li::before { content: "•"; color: var(--brand-red); margin-right: 7px; }
  .sector-list.col-a { left: 693px; }
  .sector-list.col-b { left: 823px; }

  .help { position: absolute; left: 695px; top: 722px; display: flex; align-items: center; gap: 14px; }
  .help-title { font-size: 29px; color: var(--ink); line-height: 1; }
  .help-sub { font-size: 13px; color: var(--ink); margin-top: 3px; }

  .site-footer { position: absolute; left: 0; top: 799px; width: 1200px; height: 149px; background: var(--footer-bg); }
  .copyright { position: absolute; left: 375px; top: 63px; font-size: 11px; line-height: 15px; color: var(--footer-text); }
  .footer-col { position: absolute; top: 39px; font-size: 10.5px; line-height: 14.8px; color: var(--footer-text); }
  .footer-col h4 { font-weight: 500; font-size: 10.5px; color: var(--white); }
  .footer-col ul { list-style: none; padding-left: 10px; }
  .col-software { left: 657px; }
  .col-contacts { left: 771px; }
  .col-contacts ul { width: 150px; }
  .col-resources { left: 938px; }
</style>
</head>
<body>
  <header>
    <div class="brand"><span class="brand-dot"></span><span class="brand-name">Bright Harbor Planning</span></div>
    <div class="social" aria-label="Social links"><span class="s1"></span><span class="s2"></span><span class="s3"></span><span class="s4"></span></div>
    <nav class="main-nav">
      <a href="#" style="left:162px">About Us</a>
      <a href="#" style="left:287px">Expertise</a>
      <a href="#" style="left:403px">Knowledge</a>
      <a href="#" style="left:520px">Experience</a>
      <a href="#" style="left:643px">Projects</a>
      <a href="#" style="left:744px">Focus</a>
      <a href="#" style="left:837px">Contact</a>
      <a href="#" style="left:936px">Recruitment</a>
    </nav>
  </header>

  <section class="hero" role="img" aria-label="Photo of a mine worker in orange overalls and a hard hat drilling underground">
    <div class="hero-caption">
      <h1>Bright Harbor Planning</h1>
      <p>I provide services to companies in the mining and oil and gas sector, to enabling them to plan and manage their construction projects more effectively.</p>
    </div>
    <a class="btn btn-vision" href="#">Read Our Vision</a>
    <svg class="hero-arrows" width="40" height="26" viewBox="0 0 40 26" aria-hidden="true">
      <polyline points="11,2 3,13 11,24" fill="none" stroke="#fff" stroke-width="3"/>
      <polyline points="29,2 37,13 29,24" fill="none" stroke="#fff" stroke-width="3"/>
    </svg>
  </section>

  <h2 class="section-title news-title">Latest News</h2>
  <div class="news-thumb" role="img" aria-label="Close-up photo of electronic capacitors"></div>
  <h3 class="news-headline">Exceed client’s expectations Act with integrity and honesty</h3>
  <p class="news-body">I have 20 years industry experience within engineering, construction, mining and the oil &amp; gas sector. I am well equipped to assist you and your company to deliver successful project outcomes..</p>
  <a class="btn btn-more" href="#">Read More</a>
  <a class="btn btn-all" href="#">All News</a>

  <h2 class="section-title projects-title">Projects</h2>
  <ul class="sector-list col-a">
    <li>Oil &amp; Gas</li><li>Iron Ore</li><li>Coal</li><li>Civil</li><li>Tenders</li><li>Telecomunications</li>
  </ul>
  <ul class="sector-list col-b">
    <li>New Industry</li><li>Petrochemical</li><li>Building And Constructionoil &amp; Gas</li><li>Engineering</li><li>Manufacturing</li><li>Rail</li>
  </ul>

  <div class="help">
    <svg width="46" height="46" viewBox="0 0 46 46" aria-hidden="true">
      <circle cx="23" cy="23" r="23" fill="#111"/>
      <rect x="12" y="15" width="22" height="16" rx="2" fill="#fff"/>
      <polyline points="12,16 23,25 34,16" fill="none" stroke="#111" stroke-width="2.5"/>
    </svg>
    <div>
      <div class="help-title">Need Help .</div>
      <div class="help-sub">Contact us now</div>
    </div>
  </div>

  <footer class="site-footer">
    <p class="copyright">©Copyright by 2013 Bright Harbor Planning.<br>All rights reserved</p>
    <div class="footer-col col-software"><h4>SOFTWARE</h4><ul><li>Advice</li><li>Vision</li><li>Solutions</li><li>Solutions</li><li>Perspective</li></ul></div>
    <div class="footer-col col-contacts"><h4>CONTACTS</h4><ul><li>Develop and evolve</li><li>Streamlines processes</li><li>Embrace and drive change outcomes</li></ul></div>
    <div class="footer-col col-resources"><h4>RESOURCES</h4><ul><li>Systems</li><li>Standards</li><li>Procedures</li><li>Process</li></ul></div>
  </footer>
</body>
</html>
```